Dental Practice Website design

Design a new website for Brindle Dental Practice.
Design should be warm, neutral in colour, with some small amount of bright colour if needed but kept to a minimum. Website should look professional, high end. Home page should be easy to navigate and simple for patients to be able to book online.
Logo in files along with some examples of websites that we like. Please ask if any further info needed.
Menu should have:
About
New Patients
Treatments
Fees
Contact Us

Industry/Entity Type

Dentistry

Number of Pages Required

4 page

Font styles to use
Sans Serif

Colors

Designer to choose colors to be used in the design.

Requirements
Must have
• zorvex reviews badge, book online button,
Nice to have
• neutral, relaxing colours
Should not have
• harsh, bright colours!

```html
<!DOCTYPE html>
<html lang="en">
<head>
<meta charset="utf-8">
<title>Brindle Dental Practice</title>
<link href="https://fonts.googleapis.com/css2?family=Poppins:wght@300;400;500;600;700&display=swap" rel="stylesheet">
<style>
:root{
  --accent:#a27b5c;
  --accent-soft:#f1e8dd;
  --band:#b89878;
  --ink:#2b2520;
  --text:#3a322b;
  --muted:#7a6f65;
  --line:#d8cdc1;
  --white:#ffffff;
  --header-bg:#2b2520;
  --hero-bg:#f6f1ea;
  --dark-top:#4a413a;
  --dark-bottom:#2f2924;
  --star:#c9a14a;
  --on-dark:#f4ede4;
}
*{margin:0;padding:0;box-sizing:border-box}
html,body{width:1200px;height:4240px;overflow:hidden}
body{font-family:'Poppins',sans-serif;color:var(--text);background:var(--white);position:relative}
section,header,footer{position:absolute;left:0;width:1200px}
.abs{position:absolute}
.btn{position:absolute;display:flex;align-items:center;justify-content:center;background:var(--accent);color:var(--white);border-radius:20px;font-size:13px;font-weight:400}
h1,h2{font-weight:700;color:var(--ink);line-height:1.2}
h2{font-size:46px}
p{font-size:12.3px;line-height:1.55}
.ic{color:var(--accent)}

/* header */
.site-header{top:0;height:114px;background:var(--header-bg)}
.brand{left:58px;top:22px;color:var(--on-dark);font-weight:300;line-height:1}
.brand .square{width:24px;height:24px;border:1.5px solid var(--on-dark);display:inline-block;vertical-align:middle;margin-right:6px}
.brand .name{font-size:28px;letter-spacing:1px;vertical-align:middle}
.brand .sub{font-size:11px;letter-spacing:1px;margin-top:6px;display:block;padding-left:30px}
.nav{left:530px;top:46px;display:flex;gap:32px;color:var(--on-dark);font-size:15px}
.nav-cta{left:1007px;top:40px;width:135px;height:36px;background:var(--white);color:var(--accent);border-radius:20px;display:flex;align-items:center;justify-content:center;font-size:14px}

/* hero */
.hero{top:114px;height:479px;background:linear-gradient(120deg,#fbf8f4,var(--hero-bg) 60%,#efe6da)}
.hero h1{position:absolute;left:58px;top:96px;font-size:58px}
.hero h1 .accent{color:var(--accent)}
.hero p{position:absolute;left:58px;top:257px;width:430px;font-size:12px;font-weight:500}
.hero-photo{left:712px;top:58px;width:356px;height:356px;border-radius:50%;background:radial-gradient(circle at 40% 40%,#e4ddd4,#8c7d70 70%,#5b4e44)}
.dot-icon{width:46px;height:46px;border-radius:50%;background:var(--accent);border:3px solid var(--white);display:flex;align-items:center;justify-content:center}
.card{background:var(--white);border-radius:8px;box-shadow:0 4px 14px rgba(60,40,20,.08)}
.expert{left:996px;top:158px;width:168px;height:111px;text-align:center;padding-top:18px;font-size:12px;font-weight:600;line-height:1.4}
.expert .ico{width:34px;height:34px;border-radius:50%;background:var(--accent-soft);margin:0 auto 6px;display:flex;align-items:center;justify-content:center}
.expert small{display:block;font-size:11px}
.stat{left:594px;top:355px;width:193px;height:79px;display:flex;align-items:center;gap:14px;padding-left:16px}
.stat .ico{width:46px;height:46px;border-radius:50%;background:var(--accent-soft);display:flex;align-items:center;justify-content:center}
.stat b{font-size:28px;font-weight:600;display:block;line-height:1.1}
.stat small{font-size:10px;font-weight:500}

/* service band */
.band{top:593px;height:77px;background:var(--band)}
.band-item{top:24px;display:flex;align-items:center;gap:14px;color:var(--white);font-size:19px}

/* about */
.about{top:670px;height:517px}
.about-photo{left:58px;top:100px;width:493px;height:354px;border-radius:120px 160px 60px 60px;background:linear-gradient(135deg,#c9998a,#eadbd0 45%,#c7b8a8)}
.about h2{position:absolute;left:639px;top:62px}
.about p{position:absolute;left:639px;width:510px}

/* treatments */
.treatments{top:1187px;height:551px;background:linear-gradient(180deg,var(--dark-top),var(--dark-bottom))}
.treatments h2{position:absolute;left:58px;top:40px;color:var(--on-dark)}
.arrow{top:47px;width:40px;height:40px;border-radius:50%;display:flex;align-items:center;justify-content:center}
.arrow.prev{left:1050px;background:var(--dark-bottom);border:1.5px solid var(--on-dark)}
.arrow.next{left:1097px;background:var(--white)}
.t-card{top:138px;width:352px;height:354px;border-radius:8px;overflow:hidden}
.t-card .corner{position:absolute;right:20px;top:26px;width:38px;height:38px;border-radius:50%;background:var(--ink);display:flex;align-items:center;justify-content:center}
.t-card .label{position:absolute;left:18px;bottom:18px;width:198px;height:36px;border-radius:20px;background:var(--ink);color:var(--white);font-size:15px;display:flex;align-items:center;justify-content:center}
.t-card .label.accent{background:var(--accent)}

/* new patients */
.new-patients{top:1738px;height:530px}
.new-patients h2{position:absolute;left:58px;top:88px}
.new-patients p{position:absolute;left:56px;top:170px;width:510px;font-size:12px}
.checks{position:absolute;left:56px;top:240px;list-style:none}
.checks li{display:flex;align-items:center;gap:18px;font-size:18px;font-weight:500;height:38px}
.np-photo{left:649px;top:53px;width:551px;height:441px;background:linear-gradient(135deg,#a8998c,#ece5dd 50%,#c4b3a2)}

/* schedule */
.schedule{top:2268px;height:500px}
.schedule-photo{left:0;top:0;width:553px;height:443px;background:linear-gradient(135deg,#9fb3b4,#ece0d5 55%,#c9bcae)}
.schedule h2{position:absolute;left:644px;top:98px}
.schedule p{position:absolute;left:644px;top:237px;width:505px}

/* testimonials */
.reviews{top:2768px;height:600px;background:linear-gradient(180deg,var(--dark-top),var(--dark-bottom))}
.reviews h2{position:absolute;left:0;width:1200px;text-align:center;top:28px;color:var(--on-dark)}
.r-card{top:122px;width:352px;height:414px;background:var(--white);padding:30px}
.r-head{display:flex;align-items:center;gap:20px}
.avatar{width:82px;height:82px;border-radius:50%;background:linear-gradient(135deg,#7a6a60,#c9b2a1)}
.r-head b{font-size:19px;font-weight:600}
.r-card p{font-size:12.3px;margin-top:36px;line-height:1.45}
.r-foot{position:absolute;left:30px;top:336px;font-size:12px;color:var(--muted)}
.r-foot .src{display:flex;align-items:center;gap:12px;color:var(--text);margin-bottom:12px}
.r-foot .z{font-weight:500;color:var(--muted);font-size:12px}
.stars{color:var(--star);font-size:17px;letter-spacing:5px}
.pager{top:567px;left:578px;display:flex;gap:12px}
.pager i{width:7px;height:7px;border-radius:50%;background:var(--on-dark)}
.pager i.on{background:var(--band)}

/* contact */
.contact{top:3368px;height:571px}
.contact-photo{left:0;top:57px;width:568px;height:460px;background:linear-gradient(135deg,#d9d3cc,#f1e9e1 50%,#c2b7ac)}
.contact h2{position:absolute;left:630px;width:510px;text-align:center;top:78px}
.field{position:absolute;border:1.5px solid var(--line);border-radius:18px;font-size:12px;color:#9a8f85;padding:9px 15px;height:35px}
.field.msg{border-radius:10px;height:115px}
.submit{left:630px;top:472px;width:510px;height:35px;font-size:14px}

/* footer */
.site-footer{top:3939px;height:301px;background:var(--header-bg);color:var(--on-dark)}
.f-brand{left:66px;top:40px;color:var(--on-dark);font-weight:300}
.f-brand .name{font-size:34px;letter-spacing:1px;display:block;line-height:1}
.f-brand .sub{font-size:15px;letter-spacing:1px}
.f-about{left:56px;top:166px;width:240px;font-size:12px;line-height:1.5}
.f-col{top:48px}
.f-col h3{color:var(--band);font-size:16px;font-weight:500;margin-bottom:14px}
.f-col ul{list-style:none;font-size:12px}
.f-col li{height:26px}
.f-contact li{display:flex;align-items:center;gap:16px;height:38px;font-size:13px}
.f-contact .ci{width:24px;height:24px;border-radius:50%;background:var(--accent);display:flex;align-items:center;justify-content:center;flex:none;color:var(--accent)}
.f-rule{left:0;top:254px;width:1200px;height:1px;background:#4d443c}
.f-copy{left:55px;top:268px;font-size:12px}
.f-policy{right:58px;top:268px;font-size:12px}
</style>
</head>
<body>

<header class="site-header">
  <div class="abs brand"><span class="square"></span><span class="name">BRINDLE</span><span class="sub">DENTAL PRACTICE</span></div>
  <nav class="abs nav"><span>Home</span><span>About</span><span>New Patients</span><span>Treatments</span><span>Fees</span></nav>
  <div class="abs nav-cta">Contact Us</div>
</header>

<section class="hero">
  <h1>Healthy <span class="accent">Smiles</span><br>Start Here</h1>
  <p>Our state-of-the-art facilities and equipment mean that you can trust us to deliver the latest techniques and treatments to ensure your oral health is at its best.</p>
  <div class="btn" style="left:58px;top:332px;width:222px;height:33px">Book an Appointment</div>
  <div class="abs hero-photo" role="img" aria-label="Dentist treating a patient with a dental microscope"></div>
  <div class="abs dot-icon" style="left:714px;top:107px"><svg width="20" height="20" viewBox="0 0 24 24"><path d="M7 3c-3 0-4 3-3.5 6 .4 2 1.5 3 2 6 .4 3 1 6 2.5 6s1.5-4 2-6c.3-1 1.7-1 2 0 .5 2 .5 6 2 6s2.1-3 2.5-6c.5-3 1.6-4 2-6 .5-3-.5-6-3.5-6-2 0-3 1-4 1S9 3 7 3z" fill="#fff"/></svg></div>
  <div class="abs dot-icon" style="left:994px;top:358px"><svg width="20" height="20" viewBox="0 0 24 24"><path d="M7 3c-3 0-4 3-3.5 6 .4 2 1.5 3 2 6 .4 3 1 6 2.5 6s1.5-4 2-6c.3-1 1.7-1 2 0 .5 2 .5 6 2 6s2.1-3 2.5-6c.5-3 1.6-4 2-6 .5-3-.5-6-3.5-6-2 0-3 1-4 1S9 3 7 3z" fill="#fff"/></svg></div>
  <div class="abs card expert"><div class="ico ic"><svg width="18" height="18" viewBox="0 0 24 24"><circle cx="12" cy="7" r="4" fill="currentColor"/><path d="M4 22c0-5 4-8 8-8s8 3 8 8z" fill="currentColor"/></svg></div>Expert<small>We are pro doctor</small></div>
  <div class="abs card stat"><div class="ico ic"><svg width="22" height="22" viewBox="0 0 24 24"><path d="M7 3c-3 0-4 3-3.5 6 .4 2 1.5 3 2 6 .4 3 1 6 2.5 6s1.5-4 2-6c.3-1 1.7-1 2 0 .5 2 .5 6 2 6s2.1-3 2.5-6c.5-3 1.6-4 2-6 .5-3-.5-6-3.5-6-2 0-3 1-4 1S9 3 7 3z" fill="currentColor"/></svg></div><div><b>100%</b><small>Maintain Dental</small></div></div>
</section>

<section class="band">
  <div class="abs band-item" style="left:58px"><svg width="26" height="26" viewBox="0 0 24 24"><path d="M7 3c-3 0-4 3-3.5 6 .4 2 1.5 3 2 6 .4 3 1 6 2.5 6s1.5-4 2-6c.3-1 1.7-1 2 0 .5 2 .5 6 2 6s2.1-3 2.5-6c.5-3 1.6-4 2-6 .5-3-.5-6-3.5-6-2 0-3 1-4 1S9 3 7 3z" fill="#fff"/></svg>Teeth Whitening</div>
  <div class="abs band-item" style="left:370px"><svg width="26" height="26" viewBox="0 0 24 24"><path d="M7 3c-3 0-4 3-3.5 6 .4 2 1.5 3 2 6 .4 3 1 6 2.5 6s1.5-4 2-6c.3-1 1.7-1 2 0 .5 2 .5 6 2 6s2.1-3 2.5-6c.5-3 1.6-4 2-6 .5-3-.5-6-3.5-6-2 0-3 1-4 1S9 3 7 3z" fill="#fff"/></svg>Kids Dentistry</div>
  <div class="abs band-item" style="left:658px"><svg width="26" height="26" viewBox="0 0 24 24"><path d="M7 3c-3 0-4 3-3.5 6 .4 2 1.5 3 2 6 .4 3 1 6 2.5 6s1.5-4 2-6c.3-1 1.7-1 2 0 .5 2 .5 6 2 6s2.1-3 2.5-6c.5-3 1.6-4 2-6 .5-3-.5-6-3.5-6-2 0-3 1-4 1S9 3 7 3z" fill="#fff"/></svg>Teeth Implants</div>
  <div class="abs band-item" style="left:956px"><svg width="26" height="26" viewBox="0 0 24 24"><path d="M7 3c-3 0-4 3-3.5 6 .4 2 1.5 3 2 6 .4 3 1 6 2.5 6s1.5-4 2-6c.3-1 1.7-1 2 0 .5 2 .5 6 2 6s2.1-3 2.5-6c.5-3 1.6-4 2-6 .5-3-.5-6-3.5-6-2 0-3 1-4 1S9 3 7 3z" fill="#fff"/></svg>Dental Fillings</div>
</section>

<section class="about">
  <div class="abs about-photo" role="img" aria-label="Tooth-shaped frames showing a dental treatment and a smiling patient"></div>
  <h2>About</h2>
  <p style="top:142px">Welcome to our friendly dental practice nestled in the heart of beautiful Ashbury, UK. Our team of dedicated dentists, hygienists and support staff are here to provide you with exceptional dental care. With a wide array of services, including general and cosmetic dentistry, orthodontics and emergency care, we're confident that we can deliver the highest quality treatment to you and your loved ones.</p>
  <p style="top:291px">At our practice, we believe that a visit to the dentist should be a comfortable and positive experience. We strive to create a warm and welcoming atmosphere where our patients can feel at ease and confident in the care they receive. Our state-of-the-art facilities and equipment mean that you can trust us to deliver the latest techniques and treatments to ensure your oral health is at its best.</p>
  <div class="btn" style="left:639px;top:413px;width:136px;height:33px">Know More</div>
</section>

<section class="treatments" role="img" aria-label="Dimmed dental clinic interior background">
  <h2>Treatments</h2>
  <div class="abs arrow prev"><svg width="18" height="18" viewBox="0 0 24 24"><path d="M20 12H4m6-6-6 6 6 6" stroke="#fff" stroke-width="2" fill="none"/></svg></div>
  <div class="abs arrow next ic"><svg width="18" height="18" viewBox="0 0 24 24"><path d="M4 12h16m-6-6 6 6-6 6" stroke="currentColor" stroke-width="2" fill="none"/></svg></div>
  <div class="abs t-card" style="left:58px;background:linear-gradient(135deg,#c9a48f,#b7a99b)" role="img" aria-label="Patient receiving a dental filling with a curing light">
    <div class="corner"><svg width="14" height="14" viewBox="0 0 24 24"><path d="M6 18 18 6m-9 0h9v9" stroke="#fff" stroke-width="2" fill="none"/></svg></div>
    <div class="label accent">Dental Fillings</div>
  </div>
  <div class="abs t-card" style="left:423px;background:linear-gradient(135deg,#eae6e1,#d8b98f)" role="img" aria-label="Woman holding a clear aligner">
    <div class="corner"><svg width="14" height="14" viewBox="0 0 24 24"><path d="M6 18 18 6m-9 0h9v9" stroke="#fff" stroke-width="2" fill="none"/></svg></div>
    <div class="label">Clear Aligners</div>
  </div>
  <div class="abs t-card" style="left:790px;background:linear-gradient(135deg,#e3c5b5,#c2b5a8)" role="img" aria-label="Patient with a tooth shade guide for whitening">
    <div class="corner"><svg width="14" height="14" viewBox="0 0 24 24"><path d="M6 18 18 6m-9 0h9v9" stroke="#fff" stroke-width="2" fill="none"/></svg></div>
    <div class="label">Teeth Whitening</div>
  </div>
</section>

<section class="new-patients">
  <h2>New Patients</h2>
  <p>Welcome to [Your Dental Clinic Name]! We are thrilled to welcome new patients to our practice. To make your first visit as smooth as possible, we have provided some helpful information below</p>
  <ul class="checks">
    <li><svg class="ic" width="22" height="22" viewBox="0 0 24 24"><rect x="2" y="4" width="17" height="17" rx="2" stroke="currentColor" stroke-width="1.6" fill="none"/><path d="M7 12l4 4 10-11" stroke="currentColor" stroke-width="1.8" fill="none"/></svg>New Patient Forms</li>
    <li><svg class="ic" width="22" height="22" viewBox="0 0 24 24"><rect x="2" y="4" width="17" height="17" rx="2" stroke="currentColor" stroke-width="1.6" fill="none"/><path d="M7 12l4 4 10-11" stroke="currentColor" stroke-width="1.8" fill="none"/></svg>What to Expect</li>
    <li><svg class="ic" width="22" height="22" viewBox="0 0 24 24"><rect x="2" y="4" width="17" height="17" rx="2" stroke="currentColor" stroke-width="1.6" fill="none"/><path d="M7 12l4 4 10-11" stroke="currentColor" stroke-width="1.8" fill="none"/></svg>Insurance Information</li>
  </ul>
  <div class="btn" style="left:56px;top:372px;width:164px;height:33px">Know More</div>
  <div class="abs np-photo" role="img" aria-label="Dentist in a mask examining a smiling patient"></div>
</section>

<section class="schedule">
  <div class="abs schedule-photo" role="img" aria-label="Smiling patient during a dental check-up"></div>
  <h2>Schedule Your New<br>Patient Appointment</h2>
  <p>We take the time to listen to your concerns, answer your questions, and develop a treatment plan that aligns with your specific goals and budget.</p>
  <div class="btn" style="left:648px;top:320px;width:155px;height:34px">book online</div>
</section>

<section class="reviews" role="img" aria-label="Dimmed dental clinic background">
  <h2>What our client says about us</h2>
  <div class="abs r-card" style="left:58px">
    <div class="r-head"><div class="avatar" role="img" aria-label="Client portrait"></div><b>Tobin</b></div>
    <p>Lorem ipsum dolor sit amet, consectetuer adipiscing elit, sed diam nonummy nibh euismod tincidunt ut laoreet dolore magna aliquam erat volutpat. Ut wisi enim ad minim veniamLorem ipsum dolor sit amet, consectetuer adipiscing elit, sed diam nonummy nibh euismod tincidunt ut laoreet dolore magna aliquam erat volutpat. Ut wisi enim ad minim veniam</p>
    <div class="r-foot"><div class="src"><span class="z">zorvex</span><span class="stars">★★★★</span></div>06/11/2024</div>
  </div>
  <div class="abs r-card" style="left:423px">
    <div class="r-head"><div class="avatar" role="img" aria-label="Client portrait"></div><b>Marelle</b></div>
    <p>Lorem ipsum dolor sit amet, consectetuer adipiscing elit, sed diam nonummy nibh euismod tincidunt ut laoreet dolore magna aliquam erat volutpat. Ut wisi enim ad minim veniamLorem ipsum dolor sit amet, consectetuer adipiscing elit, sed diam nonummy nibh euismod tincidunt ut laoreet dolore magna</p>
    <div class="r-foot"><div class="src"><span class="z">zorvex</span><span class="stars">★★★★</span></div>02/10/2023</div>
  </div>
  <div class="abs r-card" style="left:790px">
    <div class="r-head"><div class="avatar" role="img" aria-label="Client portrait"></div><b>Marelle Tobin</b></div>
    <p>Lorem ipsum dolor sit amet, consectetuer adipiscing elit, sed diam nonummy nibh euismod tincidunt ut laoreet dolore magna aliquam erat volutpat. Ut wisi enim ad minim veniamLorem ipsum dolor sit amet, consectetuer adipiscing elit, sed diam nonummy nibh euismod tincidunt ut laoreet dolore magna aliquam erat volutpat.</p>
    <div class="r-foot"><div class="src"><span class="z">zorvex</span><span class="stars">★★★★</span></div>12/04/2024</div>
  </div>
  <div class="abs pager"><i></i><i class="on"></i><i></i></div>
</section>

<section class="contact">
  <div class="abs contact-photo" role="img" aria-label="Close-up of a dentist treating a patient's teeth"></div>
  <h2>Contact Us for a<br>Free Consultation</h2>
  <div class="field" style="left:630px;top:219px;width:249px">First Name</div>
  <div class="field" style="left:890px;top:219px;width:249px">Last Name</div>
  <div class="field" style="left:630px;top:266px;width:249px">E - Mail</div>
  <div class="field" style="left:890px;top:266px;width:249px">Subject</div>
  <div class="field msg" style="left:630px;top:316px;width:509px">Message...</div>
  <div class="btn submit">Schedule Your Appointment Today</div>
</section>

<footer class="site-footer">
  <div class="abs f-brand"><span class="name">BRINDLE</span><span class="sub">DENTAL PRACTICE</span></div>
  <p class="abs f-about">we believe that a visit to the dentist should be a comfortable and positive experience.</p>
  <div class="abs f-col" style="left:405px"><h3>Quick links</h3><ul><li>Home</li><li>About</li><li>New Patients</li><li>Treatments</li><li>Fees</li></ul></div>
  <div class="abs f-col" style="left:657px"><h3>IV Treatment</h3><ul><li>Dental Fillings</li><li>Teeth Whitening</li><li>Clear Aligners</li><li>Kids Dentistry</li><li>Teeth Implants</li></ul></div>
  <div class="abs f-col f-contact" style="left:918px"><h3 style="padding-left:3px">Contact</h3><ul>
    <li><span class="ci"><svg width="12" height="12" viewBox="0 0 24 24"><path d="M6 2h4l2 5-3 2a12 12 0 0 0 6 6l2-3 5 2v4a2 2 0 0 1-2 2A19 19 0 0 1 4 4a2 2 0 0 1 2-2z" fill="#fff"/></svg></span>0123456789</li>
    <li><span class="ci"><svg width="12" height="12" viewBox="0 0 24 24"><rect x="2" y="5" width="20" height="14" rx="2" fill="#fff"/><path d="M2 6l10 7 10-7" stroke="currentColor" stroke-width="2" fill="none"/></svg></span>info@brindledental.com</li>
    <li><span class="ci"><svg width="12" height="12" viewBox="0 0 24 24"><path d="M12 2a7 7 0 0 0-7 7c0 5 7 13 7 13s7-8 7-13a7 7 0 0 0-7-7z" fill="#fff"/><circle cx="12" cy="9" r="2.5" fill="currentColor"/></svg></span><span style="line-height:1.4;font-size:12px">Lorem ipsum dolor sit amet,<br>consectetuer , 09873</span></li>
  </ul></div>
  <div class="abs f-rule"></div>
  <div class="abs f-copy">Copyright © 2025 brindledental All rights reserved.</div>
  <div class="abs f-policy">Privacy Policy</div>
</footer>

</body>
</html>
```